Stationery design for pet company

We need a designer for stationery designs. The name of our company is Valtrix. We specialise in pet accessories as well as distribution of pet food. We also have a brand under us for our website called Brightwhiskerclub. We will need a letterhead for Valtrix and another for Brightwhiskerclub with matching envelopes. We also would like to have a business card design with name, contact details etc with the Valtrix logo on one side of the card. The other side of the business card should have the full logo of Brightwhiskerclub with our website www.brightwhiskerclub.com.

Target Market(s)

Stationery for Valtrix is for retail shops and suppliers, therefore should have a more professional feel. Stationery for Brightwhiskerclub is mainly for customers from the website.

Industry/Entity Type

Business

Requirements
Must have
• Preferably a use of black colour for the business card.
Nice to have
• Professional feel
Should not have
• Childish designs

```html
<!DOCTYPE html>
<html lang="en">
<head>
<meta charset="utf-8">
<title>Valtrix Stationery</title>
<link href="https://fonts.googleapis.com/css2?family=Questrial&display=swap" rel="stylesheet">
<style>
:root{
  --bg:#e8e6e2;
  --paper:#ffffff;
  --ink:#2b2b2b;
  --grey:#6a6a6a;
  --faint:#ededed;
  --gold:#c9891a;
  --gold-light:#f2c458;
  --gold-dark:#a86a0c;
  --rule:#1e1e1e;
}
*{box-sizing:border-box;margin:0;padding:0}
html,body{width:1200px;height:808px;overflow:hidden}
body{background:var(--bg);font-family:"Questrial",sans-serif;color:var(--ink);position:relative}
.sheet{position:absolute;background:var(--paper);box-shadow:0 2px 10px rgba(0,0,0,.15);overflow:hidden}
.brand{display:flex;align-items:center;gap:6px;color:var(--ink);letter-spacing:.08em;text-transform:uppercase}
.brand-dot{border-radius:50%;background:var(--gold);flex:none}
.gold-band{position:absolute;left:0;right:0;bottom:0;background:linear-gradient(90deg,var(--gold-light),var(--gold) 60%,var(--gold-dark));color:#fff;display:flex;align-items:center;justify-content:flex-end;letter-spacing:.12em}
.black-rule{position:absolute;left:0;right:0;background:var(--rule)}
.faint-circle{position:absolute;border-radius:50%;border:22px solid var(--faint)}

/* Letterhead */
.letterhead{left:30px;top:40px;width:480px;height:690px}
.letterhead .head{position:absolute;right:40px;top:34px;text-align:right}
.letterhead .head .brand{justify-content:flex-end;font-size:22px}
.letterhead .head .brand-dot{width:22px;height:22px}
.letterhead .contact{font-size:7.5px;color:var(--grey);margin-top:6px;line-height:1.5}
.letterhead .body{position:absolute;left:48px;right:48px;top:180px;font-size:9.5px;line-height:1.5;color:#333;z-index:1}
.letterhead .date{margin-bottom:14px}
.letterhead .recipient{margin-bottom:18px}
.letterhead .recipient strong{font-size:11.5px;font-weight:400;color:var(--ink)}
.letterhead p{margin-bottom:11px}
.letterhead .signature{width:110px;height:34px;margin:8px 0 6px;background:linear-gradient(90deg,#f2f2f2,#e2e2e2)}
.letterhead .signer strong{font-weight:400;font-size:11px;color:var(--ink)}
.letterhead .faint-circle{right:24px;bottom:40px;width:130px;height:130px;border-width:18px}
.letterhead .black-rule{bottom:24px;height:2px}
.letterhead .gold-band{height:22px;font-size:8px;padding-right:20px}

/* Business cards */
.card{width:300px;height:172px;border-radius:10px}
.card-front{left:540px;top:40px}
.card-front .details{position:absolute;left:18px;top:22px;font-size:7.5px;line-height:1.5;color:var(--grey)}
.card-front .details .name{font-size:9px;color:var(--ink);letter-spacing:.05em}
.card-front .details .company{font-size:10px;color:var(--ink);letter-spacing:.08em;margin-top:14px}
.card-front .details .lines{margin-top:10px}
.card-front .gold-side{position:absolute;right:0;top:0;height:100%;width:150px}
.card-front .gold-side svg{position:absolute;inset:0}
.card-front .brand{position:absolute;right:12px;top:74px;color:#fff;font-size:14px}
.card-front .brand-dot{width:14px;height:14px;background:#fff}
.card-back{left:860px;top:40px;background:linear-gradient(135deg,var(--gold-light),var(--gold) 55%,var(--gold-dark))}
.card-back .club{position:absolute;left:0;right:0;top:62px;display:flex;justify-content:center;align-items:center;gap:8px;color:#fff;font-size:18px}
.card-back .club .brand-dot{width:18px;height:18px;background:#fff}
.card-back .web{position:absolute;left:0;right:0;bottom:20px;text-align:center;color:#fff;font-size:8px;letter-spacing:.15em}

/* Window envelope */
.envelope{left:540px;top:236px;width:620px;height:286px}
.envelope .brand{position:absolute;left:30px;top:34px;font-size:20px}
.envelope .brand-dot{width:20px;height:20px}
.envelope .window{position:absolute;left:64px;top:104px;width:236px;height:104px;border-radius:16px;background:linear-gradient(180deg,#f1f1f1,#e6e6e6);box-shadow:inset 0 2px 5px rgba(0,0,0,.15)}
.envelope .faint-circle{right:60px;top:60px;width:160px;height:160px}
.envelope .black-rule{bottom:38px;height:2px}
.envelope .gold-band{height:36px;font-size:8px;padding-right:22px}

/* Envelope back */
.envelope-back{left:540px;top:546px;width:380px;height:224px}
.envelope-back svg{position:absolute;left:0;top:0}
.envelope-back .brand{position:absolute;left:0;right:0;top:24px;justify-content:center;color:#fff;font-size:16px}
.envelope-back .brand-dot{width:16px;height:16px;background:#fff}
.envelope-back .return{position:absolute;left:22px;bottom:18px;font-size:7.5px;color:var(--grey);line-height:1.5}

/* Logo sheet */
.logo-sheet{left:940px;top:546px;width:220px;height:224px}
.logo-sheet .brand{position:absolute;left:0;right:0;top:96px;justify-content:center;font-size:26px;gap:8px}
.logo-sheet .brand-dot{width:26px;height:26px}
</style>
</head>
<body>

<section class="sheet letterhead" aria-label="Valtrix letterhead">
  <header class="head">
    <div class="brand"><span class="brand-dot"></span>Valtrix</div>
    <div class="contact">123, Your Street, Your City, Country 123.<br>+44(0)111 222 3333 · enquiries@valtrix.com</div>
  </header>
  <div class="faint-circle"></div>
  <div class="body">
    <div class="date">March 4, 2011</div>
    <div class="recipient"><strong>Mr Daniel Morrow</strong><br>Managing Director<br>Northfield Partners<br>42 Harbor Lane<br>Lakeport, WA 98712</div>
    <p>Lorem Ipsum is simply dummy text of the printing and typesetting industry. Lorem Ipsum has been the industry's standard dummy text ever since the 1500s, when an unknown printer took a galley of type and scrambled it to make a type specimen book. It was popularised in the 1960s and more recently with desktop publishing software.</p>
    <p>Contrary to popular belief, Lorem Ipsum is not simply random text. It has roots in a piece of classical Latin literature from 45 BC, making it over 2000 years old. Lorem Ipsum comes from sections 1.10.32 and 1.10.33 of "de Finibus Bonorum et Malorum" by Cicero, a treatise on the theory of ethics.</p>
    <p>Thank You for being one of our valued customers.</p>
    <div class="signature" role="img" aria-label="Handwritten signature"></div>
    <div class="signer"><strong>Lena Varga</strong><br>President<br>Lakeport Supplies</div>
  </div>
  <div class="black-rule"></div>
  <footer class="gold-band">www.brightwhiskerclub.com</footer>
</section>

<section class="sheet card card-front" aria-label="Business card front">
  <div class="details">
    <div class="name">YOUR NAME</div>
    <div>Position</div>
    <div>+44(0)1112223334</div>
    <div class="company">VALTRIX</div>
    <div>123, Your Street,<br>Your City, Country 123.</div>
    <div class="lines">+44(0)111 222 3333<br>enquiries@valtrix.com</div>
  </div>
  <div class="gold-side">
    <svg width="150" height="172" viewBox="0 0 150 172">
      <defs>
        <linearGradient id="cardGold" x1="0" y1="0" x2="1" y2="1">
          <stop offset="0" stop-color="#f2c458"/>
          <stop offset=".6" stop-color="#c9891a"/>
          <stop offset="1" stop-color="#a86a0c"/>
        </linearGradient>
      </defs>
      <path d="M20 0 Q70 86 20 172 L150 172 L150 0 Z" fill="url(#cardGold)"/>
      <path d="M8 0 Q58 86 8 172" fill="none" stroke="#f2c458" stroke-width="2"/>
    </svg>
  </div>
  <div class="brand"><span class="brand-dot"></span>Valtrix</div>
</section>

<section class="sheet card card-back" aria-label="Business card back">
  <div class="club"><span class="brand-dot"></span>Brightwhiskerclub</div>
  <div class="web">www.brightwhiskerclub.com</div>
</section>

<section class="sheet envelope" aria-label="Valtrix window envelope">
  <div class="brand"><span class="brand-dot"></span>Valtrix</div>
  <div class="window"></div>
  <div class="faint-circle"></div>
  <div class="black-rule"></div>
  <footer class="gold-band">www.brightwhiskerclub.com</footer>
</section>

<section class="sheet envelope-back" aria-label="Envelope back">
  <svg width="380" height="224" viewBox="0 0 380 224">
    <defs>
      <linearGradient id="flapGold" x1="0" y1="0" x2="1" y2="0">
        <stop offset="0" stop-color="#f2c458"/>
        <stop offset=".55" stop-color="#c9891a"/>
        <stop offset="1" stop-color="#a86a0c"/>
      </linearGradient>
    </defs>
    <path d="M0 0 L380 0 L380 70 Q300 120 190 96 Q80 72 0 40 Z" fill="url(#flapGold)"/>
    <path d="M0 40 Q80 72 190 96 Q300 120 380 70" fill="none" stroke="#ffffff" stroke-width="1.5"/>
  </svg>
  <div class="brand"><span class="brand-dot"></span>Valtrix</div>
  <div class="return">123, Your Street, Your City, Country 123.<br>+44(0)111 222 3333 · enquiries@valtrix.com</div>
</section>

<section class="sheet logo-sheet" aria-label="Valtrix logo">
  <div class="brand"><span class="brand-dot"></span>Valtrix</div>
</section>

</body>
</html>
```